Frostglen Fair LV, A Magical Holiday Festival

frostglenfairlv-example.com
Need to include the following:
Dates: Dec 14- Dec 30
kids 48'' and under free, presale tickets $6, glimmer pass $25(17 days pass) website: frostglenfairlv-example.com, ice skating rink, snow park, santa house, first 1000 kids will receive a gift from Santa on Christmas day.
Location: Brambleton Lodge, 4187 Quillstone Avenue.
Also need to include QRM logo and Grand Copperfield Supper Fair logo (I attached)

Industry/Entity Type

Festival

Font styles to use
Decorative

Requirements
Must have
• Date : December 14- December 30
• Location: Brambleton Lodge
Nice to have
• Santa House, christmas lights, ice skating rink, snow park

```html
<!DOCTYPE html>
<html lang="en">
<head>
<meta charset="utf-8">
<title>Frostglen Fair LV – A Magical Holiday Festival</title>
<link rel="stylesheet" href="https://fonts.googleapis.com/css2?family=Great+Vibes&family=Fjalla+One&family=Open+Sans:wght@400;600;700;800&family=Cabin+Condensed:wght@700&display=swap">
<style>
  :root {
    --red-deep: #8e0f14;
    --red-mid: #c8232a;
    --red-bright: #e43a36;
    --pine: #2f6a2c;
    --pine-dark: #173f1a;
    --gold: #c9a45a;
    --gold-light: #e3c98a;
    --ribbon: #d8282a;
    --yellow: #fef200;
    --text-yellow: #fff200;
    --white: #ffffff;
    --ink: #111111;
    --url-red: #e2231a;
    --tan: #b9855a;
  }
  * { margin: 0; padding: 0; box-sizing: border-box; }
  html, body { width: 848px; height: 1200px; overflow: hidden; background: var(--red-deep); }
  .poster {
    position: relative;
    width: 848px;
    height: 1200px;
    overflow: hidden;
    background:
      radial-gradient(ellipse 60% 45% at 50% 42%, rgba(255,110,90,0.45), rgba(255,110,90,0) 70%),
      repeating-linear-gradient(90deg, var(--red-mid) 0 22px, var(--red-deep) 22px 30px, var(--red-bright) 30px 44px, var(--red-mid) 44px 56px),
      var(--red-mid);
    font-family: "Open Sans", sans-serif;
    color: var(--white);
  }
  .poster::after {
    content: "";
    position: absolute; inset: 0;
    background: linear-gradient(180deg, rgba(0,0,0,0) 55%, rgba(80,0,0,0.45) 100%);
    pointer-events: none;
  }
  .garland-top {
    position: absolute; left: 0; top: 0; width: 848px; height: 230px;
    background: linear-gradient(180deg, var(--pine-dark) 0%, var(--pine) 70%, #3b7a35 100%);
    border-bottom-left-radius: 0 0;
    clip-path: polygon(0 0, 100% 0, 100% 100%, 80% 62%, 66% 48%, 34% 48%, 20% 62%, 0 100%);
    z-index: 1;
  }
  .bow-bells {
    position: absolute; left: 264px; top: 0; width: 296px; height: 226px;
    background: linear-gradient(180deg, var(--ribbon) 0%, var(--ribbon) 45%, var(--gold) 75%, var(--gold-light) 100%);
    border-radius: 0 0 148px 148px / 0 0 110px 110px;
    z-index: 2;
  }
  .title {
    position: absolute; left: 0; top: 196px; width: 848px;
    text-align: center; z-index: 3;
    font-family: "Great Vibes", cursive;
    font-size: 124px; line-height: 88px; font-weight: 400;
  }
  .title span { display: block; }
  .tagline {
    position: absolute; top: 430px; width: 848px; text-align: center; z-index: 3;
    font-family: "Cabin Condensed", sans-serif; font-weight: 700;
    font-size: 33px; line-height: 40px; letter-spacing: 0.5px;
  }
  .dates {
    position: absolute; top: 474px; width: 848px; text-align: center; z-index: 3;
    font-weight: 700; font-size: 74px; line-height: 84px; letter-spacing: -0.5px;
  }
  .venue {
    position: absolute; top: 562px; width: 848px; text-align: center; z-index: 3;
    font-weight: 600; font-size: 34px; line-height: 44px; color: var(--text-yellow);
  }
  .attractions {
    position: absolute; top: 608px; left: 24px; width: 800px; text-align: center; z-index: 3;
    font-family: "Fjalla One", sans-serif; font-size: 44px; line-height: 64px;
  }
  .attractions .big-number {
    font-family: "Open Sans", sans-serif; font-weight: 800; font-size: 74px; vertical-align: -5px; line-height: 64px;
  }
  .ticket-panel {
    position: absolute; left: 0; top: 832px; width: 424px; height: 368px;
    background: var(--yellow); border-top-right-radius: 40px; z-index: 4;
    color: var(--ink); text-align: center;
  }
  .ticket-panel .prices {
    position: absolute; top: 32px; left: 0; width: 412px;
    font-weight: 800; font-size: 31px; line-height: 33px;
  }
  .ticket-panel .pass-note {
    position: absolute; top: 168px; left: 0; width: 412px;
    font-size: 21px; line-height: 28px; font-weight: 400;
  }
  .ticket-panel .site {
    position: absolute; top: 206px; left: 0; width: 424px;
    font-family: "Fjalla One", sans-serif; font-size: 25px; line-height: 30px; color: var(--url-red);
  }
  .partners {
    position: absolute; top: 262px; left: 36px; width: 360px; height: 56px;
    font-family: "Fjalla One", sans-serif; color: var(--ink);
  }
  .partner-qrm { position: absolute; left: 0; top: 4px; width: 212px; font-size: 42px; line-height: 48px; letter-spacing: 6px; text-align: center; }
  .partner-supper { position: absolute; left: 228px; top: 6px; width: 140px; font-size: 16px; line-height: 19px; text-align: left; display: flex; align-items: center; gap: 8px; }
  .partner-supper .dot { width: 16px; height: 16px; border-radius: 50%; background: var(--url-red); flex: none; }
  .santa-sleigh {
    position: absolute; left: 500px; top: 826px; width: 324px; height: 300px;
    background: linear-gradient(160deg, var(--ribbon) 0%, var(--ribbon) 50%, var(--tan) 100%);
    border-radius: 36px;
    z-index: 3;
  }
  .garland-bottom {
    position: absolute; left: 392px; top: 1080px; width: 456px; height: 120px;
    background: linear-gradient(0deg, var(--pine-dark), var(--pine));
    clip-path: polygon(0 100%, 12% 40%, 40% 20%, 70% 30%, 100% 0, 100% 100%);
    z-index: 3;
  }
</style>
</head>
<body>
<main class="poster">
  <div class="garland-top" role="img" aria-label="Pine garland with golden snowflakes and twinkling lights across the top"></div>
  <div class="bow-bells" role="img" aria-label="Red ribbon bow with holly and two golden bells"></div>

  <h1 class="title"><span>Frostglen</span><span>Fair</span></h1>
  <p class="tagline">A MAGICAL HOLIDAY FESTIVAL</p>
  <p class="dates">Dec 14- Dec 30</p>
  <p class="venue">Brambleton Lodge, 4187 Quillstone Avenue.</p>
  <p class="attractions">
    Ice Skating Rink, Snow Park, Santa House,<br>
    first <span class="big-number">1000</span> kids will receive a gift from<br>
    Santa on Christmas day
  </p>

  <section class="ticket-panel">
    <p class="prices">kids 48" and<br>under free,<br>presale tickets $6,<br>glimmer pass $25</p>
    <p class="pass-note">(17 days pass)</p>
    <p class="site">FROSTGLENFAIRLV-EXAMPLE.COM</p>
    <div class="partners">
      <span class="partner-qrm">QRM</span>
      <span class="partner-supper"><span class="dot"></span>Grand Copperfield Supper Fair</span>
    </div>
  </section>

  <div class="santa-sleigh" role="img" aria-label="Cartoon Santa on a sleigh with a bag of gifts, pulled by a reindeer"></div>
  <div class="garland-bottom" role="img" aria-label="Pine branches with golden snowflakes along the bottom corner"></div>
</main>
</body>
</html>
```